Visitenkarten-Design für Hausarztpraxis
Zielgruppe
Hausarztpraxis mit Schwerpunkt Geriatrie
Zielgruppe: Patienten in einem eher ländlichen Stadtgebiet mit hoher Anzahl von Senioren
Aufgabenstellung
Idee: Kombination eines Gutscheines für eine Kaffespezialität auf der Rückseite und einer beschreibbaren Vorderseite als Bestellkärtchen mit Foto von zukünftigen "Praxisgängern" im Querschnitt. D.h. Zu sehen sein sollten 1 lustige Oma , 1 lustiger Opa (z.B. Pfeife rauchend), 1 Jugendlicher und diverse andere Erwachsene verschiedener Berufsgruppen. Beispielhaft siehe unter: Tintenfuchs: Online Terminvereinbarung-Die keine Wünsche offen lässt. Das Bild könnte auch "gezeichnet" sein. Ich würde aber ein treffendes Foto bevorzugen. Design: gut leserliche Schrift, keine verschlungene Schriftarten, wegen Lesbarkeit für Renterklientel.
Info auf der Vorderseite mit Foto: WARTEN? Nicht bei uns - Ihr persönlicher Wunschtermin:
Info auf der Rückseite (Gutschein): Gutschein für eine Kaffeespezialität (Kaffeesymbol)
farblich unterlegt, Farbe egal, passend abgestimmt zur Vorderseite
Zur Erklärung:
Die Form/ Grösse sollte die einer Visitenkarte möglichst nicht überschreiten. Gern auch eine grössere Visitenkartenform 10cm breit und 7,5 cm hoch. Das Format ist unserem Zeitdruck geschuldet. Es muss ein Werbemittel in 14 Tagen zur Praxiseröffnung zur Verfügung stehen, was sich schnell und kostengünstig produzieren und bei Bedarf ohne Probleme nachproduzieren lässt.
Sonderformate haben lange Auftragszeiten bei den auszuführenden Werbedruckfirmen.

```html
<!DOCTYPE html>
<html lang="de">
<head>
<meta charset="utf-8">
<title>Terminkarte und Gutschein – Hausarztpraxis</title>
<link href="https://fonts.googleapis.com/css2?family=Questrial&display=swap" rel="stylesheet">
<style>
  :root {
    --canvas: #ffffff;
    --teal: #aec8c7;
    --ink-light: #ffffff;
    --field-ink: #555555;
    --shadow: rgba(0, 0, 0, 0.45);
    --wood-dark: #5a2f1b;
    --wood-mid: #7e4426;
  }
  html, body {
    margin: 0;
    padding: 0;
    width: 1200px;
    height: 1200px;
    overflow: hidden;
    background: var(--canvas);
    font-family: "Questrial", "Century Gothic", sans-serif;
  }
  .sheet {
    position: relative;
    width: 1200px;
    height: 1200px;
  }
  .card {
    position: absolute;
    left: 233px;
    width: 746px;
    height: 483px;
    background: var(--teal);
    box-shadow: 2px 4px 5px var(--shadow);
    overflow: hidden;
    color: var(--ink-light);
  }
  .card--front { top: 52px; }
  .card--back { top: 599px; }

  /* Vorderseite */
  .headline {
    position: absolute;
    left: 38px;
    top: 22px;
    margin: 0;
    white-space: nowrap;
    font-weight: 400;
    line-height: 1;
  }
  .headline__question { font-size: 70px; }
  .headline__answer { font-size: 56px; margin-left: 20px; }
  .photo-band {
    position: absolute;
    left: 0;
    top: 112px;
    width: 746px;
    height: 210px;
    display: block;
  }
  .appointment-title {
    position: absolute;
    left: 35px;
    top: 322px;
    margin: 0;
    font-size: 50px;
    font-weight: 400;
    white-space: nowrap;
  }
  .field {
    position: absolute;
    top: 402px;
    width: 330px;
    height: 44px;
    background: var(--ink-light);
    color: var(--field-ink);
    font-size: 29px;
    line-height: 44px;
    padding-left: 11px;
    box-sizing: border-box;
  }
  .field--date { left: 37px; }
  .field--time { left: 379px; }

  /* Rückseite */
  .voucher-title {
    position: absolute;
    left: 0;
    width: 100%;
    top: 31px;
    margin: 0;
    text-align: center;
    font-size: 70px;
    font-weight: 400;
    line-height: 1;
  }
  .voucher-subtitle {
    position: absolute;
    left: 0;
    width: 100%;
    top: 99px;
    margin: 0;
    text-align: center;
    font-size: 36px;
  }
  .coffee-band {
    position: absolute;
    left: 0;
    top: 150px;
    width: 746px;
    height: 216px;
    display: block;
  }
  .redeem {
    position: absolute;
    left: 0;
    width: 100%;
    top: 380px;
    margin: 0;
    text-align: center;
    font-size: 36px;
  }
  .practice-address {
    position: absolute;
    left: 0;
    width: 100%;
    top: 426px;
    margin: 0;
    text-align: center;
    font-size: 25px;
    letter-spacing: 0.5px;
  }
</style>
</head>
<body>
<div class="sheet">

  <section class="card card--front">
    <h1 class="headline"><span class="headline__question">WARTEN?</span><span class="headline__answer">Nicht bei uns</span></h1>

    <svg class="photo-band" viewBox="0 0 746 210" role="img" aria-label="Fotostreifen mit fünf schräg geteilten Porträts: lachender älterer Herr mit Brille, fröhliche junge Frau, resolute Großmutter im roten Kleid, lächelnder Jugendlicher mit Kopfhörern und ein Mops mit Pfeife">
      <defs>
        <linearGradient id="panelA" x1="0" y1="0" x2="0" y2="1"><stop offset="0" stop-color="#8d9288"/><stop offset="1" stop-color="#2f3b52"/></linearGradient>
        <linearGradient id="panelB" x1="0" y1="0" x2="0" y2="1"><stop offset="0" stop-color="#9ea2ad"/><stop offset="1" stop-color="#e6dcc0"/></linearGradient>
        <linearGradient id="panelC" x1="0" y1="0" x2="0" y2="1"><stop offset="0" stop-color="#5f6f66"/><stop offset="1" stop-color="#8a2a2a"/></linearGradient>
        <linearGradient id="panelD" x1="0" y1="0" x2="0" y2="1"><stop offset="0" stop-color="#e2e2e4"/><stop offset="1" stop-color="#4e6685"/></linearGradient>
        <linearGradient id="panelE" x1="0" y1="0" x2="0" y2="1"><stop offset="0" stop-color="#3c4349"/><stop offset="1" stop-color="#c9bfa9"/></linearGradient>
      </defs>
      <polygon points="0,0 190,0 115,210 0,210" fill="url(#panelA)"/>
      <polygon points="190,0 340,0 265,210 115,210" fill="url(#panelB)"/>
      <polygon points="340,0 489,0 414,210 265,210" fill="url(#panelC)"/>
      <polygon points="489,0 637,0 562,210 414,210" fill="url(#panelD)"/>
      <polygon points="637,0 746,0 746,210 562,210" fill="url(#panelE)"/>
    </svg>

    <h2 class="appointment-title">Ihr persönlicher Wunschtermin</h2>
    <div class="field field--date">Datum:</div>
    <div class="field field--time">Uhrzeit:</div>
  </section>

  <section class="card card--back">
    <h1 class="voucher-title">GUTSCHEIN</h1>
    <p class="voucher-subtitle">für eine Kaffeespezialität</p>

    <svg class="coffee-band" viewBox="0 0 746 216" role="img" aria-label="Foto einer Tasse Kaffee mit Löffel auf Untertasse, von oben auf einem dunklen Holztisch mit verstreuten Kaffeebohnen">
      <defs>
        <linearGradient id="coffeeTone" x1="0" y1="0" x2="0" y2="1">
          <stop offset="0" stop-color="var(--wood-mid)"/>
          <stop offset="1" stop-color="var(--wood-dark)"/>
        </linearGradient>
      </defs>
      <rect width="746" height="216" fill="url(#coffeeTone)"/>
    </svg>

    <p class="redeem">Einzulösen in der Hausarztpraxis</p>
    <p class="practice-address">Konrad Wendler, 04123 Lindenstadt-Mühlau</p>
  </section>

</div>
</body>
</html>
```